Web Design Project

I need a three page website. I have designed the index.html and the specialevent.html page.

I need someone to finetune the pages for me.

Where I have difficulty is with the following:
I want to add an event table driven by php database.
The administrator of the event will login and create the wording that fits under each colmn. The administrator the submit the form to php database. The database then display in a html.

The Table contains 5 coloums and the rows can vary and can go up to as many as 100.

The table set out events on a program
In the last column of every row I need a submit button to "View and Book" I need to link those buttons with external links/pages.

I use Dreamweaver CS5 and I need to have it in this format in order for me to edit it in the future.

The Table needs to be updated once a year for this program. So ideally if someone has a password to update the certain regions this is what I have in mind.

I have also designed a mockup of the restaurant page. At the top I need.
1) 4 Colapsable panels
a) Restaurants - opening the names of the restaurants
b) Coffee shops and light lunches .... with the names
c) Family
d) Home eateries

From the colapsable panel of each of these I need a anchored link to the description/photos of each...with a BOOK now button I can submit bookings to.

I added a colapsable panel in each restaurants description to keep everything contained.

Please help

• Background must be fixed so that main.div scroll over it

The colours are chosen so please stick to it.

The green for the submit button I short is. #C8D707

I need to edit the pages in Dreamweaver CS5. /Flexilayout2pro

Please ask if you need to know anything. I exactly know what I want.

Kind regards
Marius Dreyer

The colours are fine.

The wording " havenridgeonline BOOKING agent" should appear right at the top in the white horizon part of the background image.

The specialevent page I described already. I am interested in the editable solution. for this.

I will make up a mockup of the third page and send it later.

Regards

```html
<!DOCTYPE html>
<html lang="en">
<head>
<meta charset="utf-8">
<title>Havenridge Online – Vineridge festival Program</title>
<link rel="stylesheet" href="https://fonts.googleapis.com/css2?family=Source+Sans+3:wght@300;400;600&display=swap">
<style>
:root{
  --lime:#b9c901;
  --lime-button:#C8D707;
  --olive-text:#3d4210;
  --ink:#2f2f2f;
  --charcoal:#33322d;
  --white:#ffffff;
  --rule:#e2e2e2;
  --muted:#c9c8c1;
  --body:#2b2b2b;
}
*{margin:0;padding:0;box-sizing:border-box}
html,body{width:1200px;height:1110px;overflow:hidden}
body{position:relative;background:var(--white);font-family:"Source Sans 3",sans-serif;color:var(--body)}
.landscape{position:absolute;left:0;top:112px;width:1200px;height:640px;
  background:linear-gradient(180deg,#f4f3ef 0%,#b9b7ae 10%,#8f8d84 30%,#6f6d66 60%,#8a8780 80%,#5c5a55 100%)}
.footer-band{position:absolute;left:0;top:752px;width:1200px;height:358px;background:var(--charcoal)}
.brand{position:absolute;left:104px;top:70px;font-size:38px;font-weight:400;color:var(--lime);letter-spacing:-.3px}
.main-nav{position:absolute;left:101px;top:143px;width:1005px;height:57px;border-radius:28px;background:var(--lime);box-shadow:0 2px 3px rgba(0,0,0,.25)}
.main-nav a{position:absolute;top:15px;font-size:21px;color:var(--white);text-decoration:none;transform:translateX(-50%)}
.main-nav .sep{position:absolute;top:0;width:1px;height:57px;background:rgba(90,100,0,.45)}
.content-panel{position:absolute;left:101px;top:249px;width:998px;height:520px;background:var(--white);border-radius:4px}
.page-title{position:absolute;left:0;width:100%;top:44px;text-align:center;font-size:38px;font-weight:600;color:var(--olive-text);letter-spacing:-.3px}
.program{position:absolute;left:38px;top:100px;width:926px;height:198px;border:1px solid var(--rule);border-radius:4px;background:linear-gradient(#fff 80%,#f4f4f4)}
.program-head{height:48px;background:var(--lime);border-radius:3px 3px 0 0;position:relative;color:var(--white);font-size:20px;font-weight:300}
.program-row{height:35px;border-bottom:1px solid var(--rule);position:relative;font-size:14.5px;color:#333}
.program-row:last-child{border-bottom:none}
.cell{position:absolute;top:50%;transform:translateY(-50%);white-space:nowrap}
.program-row .cell{font-weight:400}
.book-btn{position:absolute;top:50%;transform:translateY(-50%);width:114px;height:24px;background:var(--ink);color:var(--white);font-size:13px;text-align:center;line-height:24px;border-radius:2px;border-bottom:1px solid #111}
.first-row{height:43px}
.footer-panel{position:absolute;left:101px;top:732px;width:998px;height:285px}
.footer-panel svg{position:absolute;left:0;top:0}
.col{position:absolute;color:#23260a}
.col h3{font-size:23px;font-weight:400;letter-spacing:-.3px;line-height:1.1}
.col p{font-size:13.5px;font-weight:400;margin-top:7px;white-space:nowrap}
.phone{font-size:18px !important;font-weight:600 !important;margin-top:12px !important}
.email-field{margin-top:12px;width:218px;height:27px;border-radius:14px;background:var(--white);font-size:12px;color:#9a9a9a;padding:6px 15px}
.subscribe{position:absolute;left:129px;top:100px;width:90px;height:28px;border-radius:14px;background:#f4f6cf;border:1px solid #c7cc8a;font-size:14px;text-align:center;line-height:26px;color:#222}
.social{display:flex;gap:4px;margin-top:10px}
.social span{width:29px;height:29px;border-radius:50%;background:#1d1d1b}
.copyright{position:absolute;left:0;width:1200px;top:1037px;text-align:center;font-size:13px;color:var(--muted);font-weight:300}
</style>
</head>
<body>
<div class="landscape" role="img" aria-label="Sepia photograph of a small town with mountains on the horizon and houses in the foreground"></div>
<div class="footer-band"></div>

<div class="brand">Havenridge Online</div>

<nav class="main-nav">
  <a href="#" style="left:272px">Home</a>
  <span class="sep" style="left:329px"></span>
  <a href="#" style="left:438px">Accommodation</a>
  <span class="sep" style="left:542px"></span>
  <a href="#" style="left:596px">Play</a>
  <span class="sep" style="left:650px"></span>
  <a href="#" style="left:714px">Contact</a>
</nav>

<main class="content-panel">
  <h1 class="page-title">Vineridge festival Program</h1>
  <div class="program">
    <div class="program-head">
      <span class="cell" style="left:42px">Description</span>
      <span class="cell" style="left:312px">Date</span>
      <span class="cell" style="left:461px">Time</span>
      <span class="cell" style="left:592px">Price</span>
      <span class="cell" style="left:782px">Availablity</span>
    </div>
    <div class="program-row first-row">
      <span class="cell" style="left:42px">Jewellery design -2day workshop</span>
      <span class="cell" style="left:312px">Friday 02 August</span>
      <span class="cell" style="left:463px">14hoo-16h30</span>
      <span class="cell" style="left:605px">Rs 200 pp</span>
      <span class="book-btn" style="left:779px">Availablity</span>
    </div>
    <div class="program-row">
      <span class="cell" style="left:42px">Cupcake fun</span>
      <span class="cell" style="left:312px">Sat 03 August</span>
      <span class="cell" style="left:463px">09h00- 14hoo</span>
      <span class="cell" style="left:605px">Rs 30 pp</span>
      <span class="book-btn" style="left:779px">Availablity</span>
    </div>
    <div class="program-row">
      <span class="cell" style="left:42px">Harvest dance</span>
      <span class="cell" style="left:312px">Sat 03 August</span>
      <span class="cell" style="left:463px">18h00-22h00</span>
      <span class="cell" style="left:605px">Rs 500 pp</span>
      <span class="book-btn" style="left:781px">Availablity</span>
    </div>
  </div>
</main>

<footer class="footer-panel">
  <svg width="998" height="285" viewBox="0 0 998 285" aria-hidden="true">
    <defs>
      <linearGradient id="footerGreen" x1="0" y1="0" x2="0" y2="1">
        <stop offset="0" stop-color="#d6e70e"/>
        <stop offset="1" stop-color="#b3c400"/>
      </linearGradient>
    </defs>
    <path d="M0 20 Q499 6 998 20 L998 268 Q998 276 988 277 Q499 302 10 277 Q0 276 0 268 Z" fill="#e9f08a"/>
    <path d="M0 26 Q499 12 998 26 L998 262 Q998 272 988 273 Q499 296 10 273 Q0 272 0 262 Z" fill="url(#footerGreen)"/>
  </svg>
  <div class="col" style="left:48px;top:66px">
    <h3>Contact Us</h3>
    <p class="phone">0861 372910</p>
    <p>email: admin@havenridge.biz</p>
    <p>address: Mill Street, Havenridge</p>
  </div>
  <div class="col" style="left:303px;top:66px">
    <h3>Services List</h3>
    <p style="margin-top:12px">Business Directory</p>
    <p>Relevant links and websites</p>
    <p>Emergency Numbers</p>
  </div>
  <div class="col" style="left:517px;top:62px">
    <h3>Newsletter Sign Up</h3>
    <p style="font-size:13px;margin-top:8px">Please sign up here for latest news</p>
    <div class="email-field">email address</div>
    <div class="subscribe">Subscribe</div>
  </div>
  <div class="col" style="left:783px;top:60px">
    <h3>Get in Touch</h3>
    <div class="social"><span></span><span></span><span></span><span></span></div>
  </div>
</footer>

<div class="copyright">Copyright © 2013 Company Name.&nbsp; All right reserved.</div>
</body>
</html>
```